Raw Food & Health Coach Needs a Clutch Coupon

I need a clutch coupon for a raw food & health coaching business based in Washington, DC called Cora Penwick, LLC. I help ladies and gents on the go who want to support their bodies to stay healthy or prevent/correct disease so they can live extraordinary lives while deeply serving the world. My services include individual coaching, (online) group coaching, and corporate wellness coaching.

I would like to create a clutch coupon to give to referral partners who in turn will give them to their clients. So far I have two referral partners in mind: Marcus Elvey Salon & Spa; and Colon Hydrotherapist Wendy Tasbrook.

Marcus Elvey Salon & Spa will be having an event on Thursday, September 12, 2013, during which time their clients who get a hair cut will receive a complimentary Velunique (hair) Treatment & a complimentary Radiant Through and Through Planning Hour with me.

I would like to see designs that use 2-4 colors, including a bit of green. The final design should communicate beauty/health from the inside out and boundless energy to enjoy an extraordinary life. It should be natural yet elegant/classy.

Designers are currently working on my business logo. The logo design project has not yet been completed. Once it completes, I will send the logo design to you and request that you incorporate the logo into your coupon design.

IMPORTANT: I need to select a winning design on Wed, Sept 11, 2013, and get the source files from the designer within 24 hours (before Thursday, Sept 12 MORNING); so that I have time to adjust any text and take it to the printer in order to distribute the coupon later that afternoon. I will need the source files urgently (within the next 24 hours).

Then after the event the designer will make the changes on the design for me incorporating my logo for use with multiple referral partners. I will approve the Payment when I have finalized the design

To repeat, I must have the winning design on September 11 (or Sept 12 morning at the latest).

IMPORTANT: Refer to uploaded Referral Partner Clutch Coupon SAMPLE to give you an idea of the layout I'd like, but PLEASE don't let it stifle YOUR creativity.
Updates

The focus should be on the Free Radiant Through and Through Planning Hour, not on me.

 

I think I’d prefer a white background and black text, unless you can convince me otherwise by showing me a beautiful design.

 

Ensure there is space between paragraphs.

 

Somehow differentiate my free gift (Wellbeing Guard Starter Kit), phone and URL at the bottom on the back. While it would be nice to include my free gift, I may have to leave out if it won’t fit on the coupon.

Target Market(s)

The audience is busy, heart-centered/socially responsible professional men and women on the go who hardly have time for self-care, but who will pay for holistic services (alternative therapies) to enhance their beauty/health so that they can perform their best while deeply serving the world without getting sick or having to endure toxic therapies like surgery, chemotherapy, radiation, and pills.

Industry/Entity Type

Printer

Requirements
Must have
• 2-4 colors, including a little green

Dimensions: approx. 2.25 inches x 5.25 inches.

Text from the uploaded file. Note: I'm not sure if all the text I've provided will fit nicely on the back of the coupon. If no then please increase the dimensions as little as possible.

The front of the coupon designed horizontally, and the back designed vertically.
Nice to have
• I'm open to your using illustrations or photos of the raw food and/or lifestyle tools that I use with clients in my business, such as green juice, (leafy) green veggies, cucumbers, lemons, berries, green smoothies, superfoods, movement/exercise, self-care...

I also like the idea of including a face in the design. When I’ve surveyed in the past people have related better to a face than just to a bowl of veggies or fruit.
Should not have
• the colors orange or red, or florescent colors.

```html
<!DOCTYPE html>
<html lang="en">
<head>
<meta charset="utf-8">
<title>Cora Penwick – Raw Food &amp; Health Coach Clutch Coupon</title>
<link href="https://fonts.googleapis.com/css2?family=Poiret+One&family=Ubuntu:wght@400;700&display=swap" rel="stylesheet">
<style>
  :root {
    --backdrop: #8a6a4c;
    --card: #ffffff;
    --card-shade: #e9e9e9;
    --ink: #111111;
    --green: #1f6e32;
    --link: #3d4ea3;
    --frame: #ffffff;
    --photo-tone-a: #6b4a3a;
    --photo-tone-b: #c79a82;
    --fruit-a: #f2f2ee;
    --fruit-b: #d9a24a;
    --fruit-c: #8fbf4a;
  }
  * { box-sizing: border-box; margin: 0; padding: 0; }
  html, body {
    width: 1200px; height: 783px; overflow: hidden;
    background: var(--backdrop);
  }
  .stage { position: relative; width: 1200px; height: 783px; }

  /* Front of coupon */
  .coupon-front {
    position: absolute; left: 63px; top: 237px; width: 704px; height: 300px;
    background: linear-gradient(180deg, var(--card) 0%, var(--card) 45%, var(--card-shade) 100%);
    box-shadow: 0 2px 6px rgba(0,0,0,.35);
    font-family: "Ubuntu", sans-serif;
    color: var(--green);
  }
  .coach-portrait {
    position: absolute; left: 17px; top: 16px; width: 99px; height: 103px;
    background: var(--frame); padding: 4px;
    box-shadow: 1px 2px 4px rgba(0,0,0,.35);
  }
  .coach-portrait .fill {
    width: 100%; height: 100%;
    background: linear-gradient(160deg, var(--photo-tone-a), var(--photo-tone-b) 55%, var(--photo-tone-a));
  }
  .coach-name {
    position: absolute; left: 137px; top: 4px;
    font-family: "Poiret One", sans-serif; font-size: 66px; font-weight: 400;
    color: var(--ink); letter-spacing: 1px; white-space: nowrap;
  }
  .coach-title {
    position: absolute; left: 138px; top: 80px;
    font-family: "Poiret One", sans-serif; font-size: 40px;
    color: var(--ink); letter-spacing: 1.5px; white-space: nowrap;
  }
  .offer-line {
    position: absolute; left: 27px; white-space: nowrap; font-size: 20px;
  }
  .offer-line strong { font-weight: 700; }
  .offer-line.l1 { top: 139px; }
  .offer-line.l2 { top: 164px; }
  .offer-line.l3 { top: 199px; font-size: 21px; }
  .offer-line.l4 { top: 230px; font-size: 21px; }
  .offer-line.l5 { top: 263px; font-size: 21px; }
  .booking-link { color: var(--link); font-weight: 700; margin-left: 10px; }
  .fruit-visual {
    position: absolute; left: 532px; top: 178px; width: 170px; height: 116px;
    background: radial-gradient(ellipse at 55% 30%, var(--fruit-a) 0 22%, transparent 23%),
                radial-gradient(ellipse at 50% 80%, var(--fruit-b), var(--fruit-c) 60%, transparent 75%);
  }

  /* Back of coupon */
  .coupon-back {
    position: absolute; left: 822px; top: 37px; width: 300px; height: 701px;
    background: var(--card);
    box-shadow: 0 2px 6px rgba(0,0,0,.35);
    font-family: "Ubuntu", sans-serif; color: var(--green);
    padding: 6px 0 0 14px;
    font-size: 12.7px; line-height: 15.6px;
  }
  .coupon-back h2 { font-size: 12.7px; font-weight: 700; }
  .coupon-back p { margin-bottom: 15.6px; }
  .benefit-list { list-style: none; margin: 0 0 14px 0; }
  .benefit-list li { padding-left: 16px; position: relative; }
  .benefit-list li::before { content: "•"; position: absolute; left: 1px; }
  .back-cta { font-size: 20px; line-height: 24px; }
  .back-cta .booking-link { display: block; margin: 0; }
  .back-contact { font-size: 18px; margin-top: 14px; }
</style>
</head>
<body>
<main class="stage">

  <section class="coupon-front" aria-label="Coupon front">
    <div class="coach-portrait"><div class="fill" role="img" aria-label="Portrait photo of the coach"></div></div>
    <h1 class="coach-name">Cora Penwick</h1>
    <div class="coach-title">Raw Food &amp; Health Coach</div>
    <p class="offer-line l1">Free Radiant Through and Through Planning Hour</p>
    <p class="offer-line l2">with <strong>Certified Raw Food &amp; Health Coach</strong>, Cora Penwick.</p>
    <p class="offer-line l3">30 minutes, focused entirely on you <strong>(a $50 value, free).</strong></p>
    <p class="offer-line l4">Compliments of <strong>Marcus Elvey Salon &amp; Spa</strong></p>
    <p class="offer-line l5">Schedule your appointment: <span class="booking-link">http://bit.ly/RTtPH</span></p>
    <div class="fruit-visual" role="img" aria-label="Glass of milky smoothie with fresh fruit: citrus, strawberries and limes"></div>
  </section>

  <section class="coupon-back" aria-label="Coupon back">
    <h2>What is Raw Food &amp; Health Coaching?</h2>
    <p>Raw food coaching helps you go or stay raw to<br>the level that you truly desire.</p>
    <p>Health couching helps you connect the dots<br>between what you eat and how you feel. You’ll<br>know how to detoxify your body, boost your<br>immune system, multiply your energy, im-<br>prove your mood, gravitate to the perfect<br>body weight for you, and delight in what you<br>eat like never before – without restriction.</p>
    <h2>Who benefits from this work?</h2>
    <p>Ladies and gents on the go who want to<br>enable their bodies to prevent or correct dis-<br>ease and create abundant energy so they can<br>live extraordinary lives while deeply serving<br>the world.</p>
    <p>Raw food is literally for everyone, but the<br>degree to which someone goes raw and for<br>what duration is a very personal decision. This<br>is about what works for you, what feels right<br>for you and what get you to where you want<br>to be.</p>
    <p style="margin-bottom:0">Generally speaking, raw food is great for<br>anyone who wants to…</p>
    <ul class="benefit-list">
      <li>Correct or prevent a serious disease</li>
      <li>Look and/or feel better</li>
      <li>Look/feel 10 years younger</li>
      <li>Fit into their skinny jeans without dieting</li>
      <li>Double their energy</li>
      <li>Reduce their cravings</li>
      <li>Detox their body</li>
      <li>Think more clearly</li>
      <li>Get a lot done without having a lot of time</li>
      <li>Feel happier</li>
    </ul>
    <div class="back-cta">Schedule your appointment:<span class="booking-link">http://bit.ly/RTtPH</span></div>
    <div class="back-contact">202-555-0147, corapenwick.com</div>
  </section>

</main>
</body>
</html>
```